Plakat-Design: Hausmesse Robotik und Cobots
Zielgruppe
High-Tech Engineering aus Euskirchen
Die KW Konstrukteure & Fachservice GmbH mit Sitz in Euskirchen entwickelt moderne Maschinen Robotiklösungen für Kunden in der Region, überregional und bundesweit. Mittelständische Unternehmen und Maschinenbauer, internationale Großkonzerne aus der Konsumgüterindustrie und Hersteller von Maschinen für die weiterverarbeitende Industrie vertrauen KW seit vielen Jahren.
> Maschinenbau
> Automation
> Robotik
> Certified Systemintegrator für Brennwald Mechatronik
Aufgabenstellung
Projektauftrag:
Flyer/Plakat zur Einladung Hausmesse
Format:
> Din A4 PDF zur Einladung der Kunten (digital)
> Werbebanner für E-Mail Signatur
Daten der Messe:
> 18.05.2022 10-17 Uhr
> KW Technik , Lindenhofer Weg 14, 53879 Euskirchen
> Anmeldeplattform folgt
Motto der Veranstaltung:
> 'Automation - so einfach'
> 'Einfach automatisieren mit Cobots'
> Für Vorschläge gerne offen
Was erwartet Sie:
> Roboter Demos
> Kamerageführte Robotik
> Plug & Play Lösungen
Ausstellerinformationen:
> Bitte unten Platz für Logos der Aussteller vorsehen (derzeit ca. 15)
> Logos können später übermittelt werden
Infomaterial für den Designer:
>> www.kw-technik-beispiel.de
>> www.brennwald-mechatronik-beispiel.de
>> Weitere Bilder sind vorhanden.
>> Farbeschema der PowerPoint nutzen (Vertriebspräsentation_de_KW_21-06-23.pptx)

```html
<!DOCTYPE html>
<html lang="de">
<head>
<meta charset="utf-8">
<title>Hausmesse Robotik – Automation so einfach</title>
<link href="https://fonts.googleapis.com/css2?family=Montserrat:wght@300;400;500;600;700&family=Roboto:wght@500&display=swap" rel="stylesheet">
<style>
  :root {
    --brand-blue: #2d4d9b;
    --ink: #333333;
    --ink-soft: #444444;
    --panel-dark: #323232;
    --panel-light: #f1f1f1;
    --white: #ffffff;
    --logo-navy: #1b2b4f;
    --logo-violet: #7b4be0;
    --logo-blue: #2f6fe0;
    --logo-orange: #e2983a;
  }
  * { margin: 0; padding: 0; box-sizing: border-box; }
  html, body { width: 1175px; height: 1200px; overflow: hidden; background: var(--white); }
  body { position: relative; font-family: "Montserrat", sans-serif; color: var(--ink); }

  .poster {
    position: absolute; left: 240px; top: 99px; width: 694px; height: 982px;
    background: linear-gradient(180deg, var(--panel-light) 0%, #fafafa 100%);
    box-shadow: 0 4px 18px rgba(0,0,0,0.18);
    overflow: hidden;
  }

  .highlights {
    position: absolute; left: 0; top: 0; width: 100%; height: 65px;
    background: var(--brand-blue);
    display: flex; align-items: center; justify-content: space-between;
    padding: 0 23px;
    font-family: "Roboto", sans-serif; font-weight: 500; font-size: 16px;
    color: var(--white); letter-spacing: 0.1px;
  }
  .highlight { display: flex; align-items: center; gap: 14px; }
  .highlight svg { width: 20px; height: 20px; }

  .hero-photo {
    position: absolute; left: 0; top: 65px; width: 100%; height: 326px;
    background:
      radial-gradient(ellipse at 45% 45%, #8c98ad 0%, transparent 55%),
      linear-gradient(100deg, #5d6e8e 0%, #9aa7bd 35%, #4a5c80 60%, #8595b2 100%);
  }

  .headline-band {
    position: absolute; left: 0; top: 391px; width: 100%; height: 121px;
    background: var(--brand-blue); color: var(--white);
    padding: 26px 0 0 48px;
  }
  .headline { font-weight: 700; font-size: 41px; line-height: 1.05; }
  .subline { font-weight: 300; font-size: 29px; line-height: 1.3; margin-top: 1px; }

  .date-box {
    position: absolute; left: 0; top: 512px; width: 326px; height: 83px;
    background: var(--panel-dark); color: var(--white);
    font-weight: 300; font-size: 39px; padding: 18px 0 0 47px;
  }
  .host {
    position: absolute; left: 326px; top: 512px; width: 368px; height: 83px;
    background: var(--white);
    display: flex; align-items: center; gap: 14px; padding-left: 24px;
  }
  .host-name { font-weight: 700; font-size: 17px; color: var(--brand-blue); white-space: nowrap; display: flex; align-items: center; gap: 7px; }
  .host-name::before { content: ""; width: 13px; height: 13px; background: var(--brand-blue); display: block; }
  .host-claim { font-weight: 600; font-size: 10.5px; line-height: 1.4; color: var(--ink-soft); white-space: nowrap; }
  .host-claim strong { color: var(--brand-blue); font-weight: 700; }

  .details { position: absolute; left: 0; top: 634px; width: 694px; }
  .detail-block { position: absolute; top: 0; }
  .detail-block h2 { font-weight: 600; font-size: 21px; line-height: 28px; color: var(--ink); margin-bottom: 1px; }
  .detail-block p { font-weight: 400; font-size: 19px; line-height: 28px; color: var(--ink-soft); }
  .where { left: 46px; }
  .when { left: 357px; }
  .when table { border-collapse: collapse; font-size: 19px; color: var(--ink-soft); }
  .when td { padding: 0; line-height: 28px; }
  .when td:first-child { width: 114px; }

  .exhibitors-title {
    position: absolute; left: 46px; top: 753px; width: 602px;
    display: flex; align-items: center; gap: 24px;
    font-weight: 600; font-size: 21px; line-height: 28px; color: var(--ink);
  }
  .exhibitors-title::after { content: ""; flex: 1; height: 1px; background: #d8d8d8; }

  .exhibitor-grid {
    position: absolute; left: 46px; top: 806px; width: 625px;
    display: grid; grid-template-columns: repeat(5, 125px); grid-auto-rows: 26px; row-gap: 28px;
  }
  .exhibitor {
    display: flex; align-items: center; gap: 6px; height: 26px;
    font-weight: 700; font-size: 12.5px; color: var(--logo-navy);
  }
  .exhibitor::before { content: ""; width: 16px; height: 16px; border-radius: 50%; flex: none; }
  .exhibitor.violet::before { background: var(--logo-violet); }
  .exhibitor.blue::before { background: var(--logo-blue); }
  .exhibitor.orange::before { background: var(--logo-orange); }
  .exhibitor.navy::before { background: var(--logo-navy); }
</style>
</head>
<body>
  <main class="poster">
    <header class="highlights">
      <div class="highlight">
        <svg viewBox="0 0 20 20" aria-hidden="true"><circle cx="10" cy="10" r="8.5" fill="none" stroke="#fff" stroke-width="1.6"/><path d="M6 10.2l2.7 2.6L14 7.5" fill="none" stroke="#fff" stroke-width="1.6"/></svg>
        <span>ROBOTER DEMOS</span>
      </div>
      <div class="highlight">
        <svg viewBox="0 0 20 20" aria-hidden="true"><circle cx="10" cy="10" r="8.5" fill="none" stroke="#fff" stroke-width="1.6"/><path d="M6 10.2l2.7 2.6L14 7.5" fill="none" stroke="#fff" stroke-width="1.6"/></svg>
        <span>KAMERAGEFÜHRTE ROBOTIK</span>
      </div>
      <div class="highlight">
        <svg viewBox="0 0 20 20" aria-hidden="true"><circle cx="10" cy="10" r="8.5" fill="none" stroke="#fff" stroke-width="1.6"/><path d="M6 10.2l2.7 2.6L14 7.5" fill="none" stroke="#fff" stroke-width="1.6"/></svg>
        <span>PLUG &amp; PLAY</span>
      </div>
    </header>

    <div class="hero-photo" role="img" aria-label="Foto: Cobot-Roboterarm mit Greifer in einer Fertigungshalle, blau getönt"></div>

    <section class="headline-band">
      <h1 class="headline">Automation - So einfach.</h1>
      <p class="subline">Einfach automatisieren mit Cobots</p>
    </section>

    <div class="date-box">18.MAI.2022</div>
    <div class="host">
      <span class="host-name">KW Technik</span>
      <p class="host-claim"><strong>KW Technik &amp; Dienstleistungen -</strong><br>Wir realisieren Ihre Projekte</p>
    </div>

    <section class="details">
      <div class="detail-block where">
        <h2>Wo?</h2>
        <p>Lindenhofer Weg 14<br>53879 Euskirchen</p>
      </div>
      <div class="detail-block when">
        <h2>Wann?</h2>
        <table>
          <tr><td>Beginn</td><td>10:00 UHR</td></tr>
          <tr><td>Ende</td><td>17:00 UHR</td></tr>
        </table>
      </div>
    </section>

    <h2 class="exhibitors-title">Die Aussteller</h2>
    <div class="exhibitor-grid">
      <span class="exhibitor violet">Logoipsum</span>
      <span class="exhibitor violet">Logoipsum</span>
      <span class="exhibitor blue">logoipsum</span>
      <span class="exhibitor blue">logoipsum</span>
      <span class="exhibitor blue">logoipsum</span>
      <span class="exhibitor blue">logoipsum</span>
      <span class="exhibitor blue">logoipsum</span>
      <span class="exhibitor blue">logoipsum</span>
      <span class="exhibitor blue">logoipsum</span>
      <span class="exhibitor blue">logoipsum</span>
      <span class="exhibitor navy">logoipsum</span>
      <span class="exhibitor navy">logoipsum</span>
      <span class="exhibitor orange">Logo Ipsum</span>
      <span class="exhibitor orange">Logo Ipsum</span>
      <span class="exhibitor orange">Logo Ipsum</span>
    </div>
  </main>
</body>
</html>
```